Travel Company is looking for a STAND OUT Business Card

I need a unique Business Card that will truly stand out. Nothing too busy. Simple is good, right? Not looking for a standard design either. No cookie cutter layout. We are a Travel Company that works more with Companies than Travelers. I had an idea to focus and emphasis on the 2 logo a bit more. This is not necessary, however thought it would look interesting. I am just looking for something interesting and a bit different. Does't have to completely off the wall crazy, just not your run of the mill business card.

Target Market(s)

Hoteliers, Resort Management, Call Centers, Executives, Travelers, Families, Businesses

Industry/Entity Type

Hospitality

Contact Information for Business Card

President/CEO - Marcus T Bellamy (title not necessary if design doesn't allow for it)
contact - (407) 555-0186
email - mbellamy@wayfarenow.example
address - 4812 Quillmore Ave #164
Orlando, FL 32804
website - www.wayfarenow.example

Font styles to use
Serif
Other font styles liked:
• Avenir Next LT Pro BOLD

Requirements
Must have
• simple look and design. Unique design
Nice to have
• I attached the 2 logo separate from the main logo. This can be used separately from the Main Logo, together with the main logo or as main logo. I included the logo font. Use it or not, designers choice.
Should not have
• cookie cutter design. Little use of red other than the logo

```html
<!DOCTYPE html>
<html lang="en">
<head>
<meta charset="utf-8">
<title>Wayfare Now – Business Card</title>
<link rel="stylesheet" href="https://fonts.googleapis.com/css2?family=Open+Sans:wght@400;700&display=swap">
<style>
  :root {
    --backdrop: #dcdcdc;
    --card: #efefef;
    --map: #cfd0d2;
    --red: #ec1a45;
    --ink: #111111;
    --dark: #2e2226;
    --white: #ffffff;
  }
  * { box-sizing: border-box; margin: 0; padding: 0; }
  html, body { width: 1200px; height: 900px; overflow: hidden; }
  body {
    background: var(--backdrop);
    font-family: "Open Sans", Arial, sans-serif;
    display: flex;
    flex-direction: column;
    align-items: center;
    justify-content: center;
    gap: 50px;
  }
  .card {
    position: relative;
    width: 640px;
    height: 366px;
    background: var(--card);
    overflow: hidden;
    box-shadow: 0 2px 6px rgba(0,0,0,0.12);
  }
  .card svg.shapes { position: absolute; inset: 0; }
  .map-area {
    position: absolute;
    background: radial-gradient(ellipse at center, var(--map) 0%, rgba(207,208,210,0.55) 55%, rgba(239,239,239,0) 80%);
  }
  .front .map-area { left: 60px; top: 0; width: 480px; height: 250px; }
  .back .map-area { left: 70px; top: 20px; width: 540px; height: 330px; }

  .identity { position: absolute; left: 40px; top: 44px; display: flex; align-items: flex-start; gap: 8px; }
  .identity .pin { width: 22px; height: 30px; margin-top: 2px; }
  .name { font-weight: 700; font-size: 30px; color: var(--ink); line-height: 1.1; letter-spacing: -0.3px; white-space: nowrap; }
  .title { font-size: 12px; color: #444; margin-top: 2px; }

  .contacts { position: absolute; left: 376px; top: 62px; width: 248px; list-style: none; color: var(--white); font-size: 13px; }
  .contacts li { display: flex; align-items: center; gap: 10px; height: 30px; white-space: nowrap; }
  .contacts svg { width: 15px; height: 15px; flex: none; }

  .address {
    position: absolute; left: 62px; top: 234px;
    display: flex; align-items: center; gap: 12px;
    color: var(--white); font-size: 18px; white-space: nowrap;
  }
  .address svg { width: 14px; height: 18px; }

  .brand {
    position: absolute; left: 0; right: 0; top: 150px;
    display: flex; align-items: center; justify-content: center; gap: 14px;
  }
  .brand .dot { width: 40px; height: 40px; border-radius: 50%; background: var(--red); }
  .brand .wordmark { font-weight: 700; font-size: 52px; color: var(--ink); letter-spacing: -1px; }
</style>
</head>
<body>

<section class="card front" aria-label="Business card front">
  <div class="map-area" role="img" aria-label="Faint grey world map"></div>
  <svg class="shapes" viewBox="0 0 640 366" width="640" height="366" aria-hidden="true">
    <polygon points="0,0 48,0 26,30 0,30" fill="var(--red)"/>
    <polygon points="392,0 640,0 640,366 300,366 300,120" fill="var(--dark)"/>
    <polygon points="28,212 560,212 560,286 28,286" fill="var(--red)"/>
  </svg>

  <div class="identity">
    <svg class="pin" viewBox="0 0 22 30" aria-hidden="true">
      <path d="M11 2a8.5 8.5 0 0 1 8.5 8.5c0 6-8.5 16-8.5 16S2.5 16.5 2.5 10.5A8.5 8.5 0 0 1 11 2z" fill="none" stroke="#555" stroke-width="3"/>
    </svg>
    <div>
      <div class="name">Marcus T Bellamy</div>
      <div class="title">President/CEO</div>
    </div>
  </div>

  <ul class="contacts">
    <li>
      <svg viewBox="0 0 16 16" aria-hidden="true"><circle cx="8" cy="8" r="7" fill="none" stroke="#fff" stroke-width="1.4"/><path d="M5.5 4.5l1.5 0 .6 2-1 .8a5 5 0 0 0 2.2 2.2l.8-1 2 .6v1.5c-3.6 .3-6.4-2.5-6.1-6.1z" fill="#fff"/></svg>
      <span>(407) 555-0186</span>
    </li>
    <li>
      <svg viewBox="0 0 16 16" aria-hidden="true"><rect x="1" y="3" width="14" height="10" fill="#fff"/><path d="M1 3l7 6 7-6" fill="none" stroke="#2e2226" stroke-width="1.2"/></svg>
      <span>mbellamy@wayfarenow.example</span>
    </li>
    <li>
      <svg viewBox="0 0 16 16" aria-hidden="true"><g fill="none" stroke="#fff" stroke-width="1.3"><circle cx="8" cy="8" r="7"/><ellipse cx="8" cy="8" rx="3" ry="7"/><path d="M1 8h14M2.5 4.5h11M2.5 11.5h11"/></g></svg>
      <span>www.wayfarenow.example</span>
    </li>
  </ul>

  <div class="address">
    <svg viewBox="0 0 14 18" aria-hidden="true"><path d="M7 0a6 6 0 0 1 6 6c0 4.5-6 12-6 12S1 10.5 1 6a6 6 0 0 1 6-6z" fill="#fff"/><circle cx="7" cy="6" r="2.2" fill="#ec1a45"/></svg>
    <span>4812 Quillmore Ave #164 Orlando, FL 32804</span>
  </div>
</section>

<section class="card back" aria-label="Business card back">
  <div class="map-area" role="img" aria-label="Faint grey world map"></div>
  <svg class="shapes" viewBox="0 0 640 366" width="640" height="366" aria-hidden="true">
    <polygon points="0,0 60,0 80,40 48,150 0,150" fill="var(--red)"/>
    <polygon points="0,212 80,212 100,366 0,366" fill="var(--red)"/>
    <polygon points="590,300 640,300 640,366 580,366" fill="var(--red)"/>
  </svg>
  <div class="brand">
    <span class="dot" aria-hidden="true"></span>
    <span class="wordmark">Wayfare Now</span>
  </div>
</section>

</body>
</html>
```